Flyer für Wahlkampf
Zielgruppe
Ich benötige den Flyer für den Wahlkampf. Ich bin Kandidat für die Kommunalwahlen (Gemeinderats- und Kreistagswahl).
Aufgabenstellung
Der Flyer soll das Format DIN A5 haben und vier Seiten umfassen. Er soll einmal in der Mitte faltbar sein. Ob der Flyer in Hoch- oder Querformat erstellt wird, überlasse ich der Kreativität der Designer.
Die erste Seite soll das im Anhang beigefügte Bild von mir enthalten sowie die Angaben im beigefügten Word-Dokument. Idealerweise soll das Bild die ganze Seite einnehmen und die Angaben erscheinen an der Seite auf dem Bild. Ich überlasse dies jedoch der Kreativität der Designer.
Auf der zweiten Seite sollen die im Anhang beigefügten restlichen Bilder unter der Ruprik 'Meine bisherigen Erfolge für unsere Ortschaft:' erscheinen.
Der restliche Flyer soll dann nur aus Text bestehen, welcher kreativ angeordnet werden kann.
Allgemein habe ich hinsichtlich der Schriftart keine Vorstellungen und überlasse dies der Kreativität der Designer.
Dankeschön! :-)

```html
<!DOCTYPE html>
<html lang="de">
<head>
<meta charset="utf-8">
<title>Wahlkampf-Flyer Lukas Brandt</title>
<link href="https://fonts.googleapis.com/css2?family=Archivo+Black&family=Roboto+Condensed:wght@400;700;800&display=swap" rel="stylesheet">
<style>
  :root{
    --yellow:#f6c11a;
    --dark:#2a2a2a;
    --ink:#1a1a1a;
    --paper:#ffffff;
    --photo-top:#6d6d6d;
    --photo-bottom:#3f4146;
    --stage:#e6e6e6;
  }
  *{box-sizing:border-box;margin:0;padding:0}
  html,body{width:1200px;height:840px;overflow:hidden;background:var(--stage)}
  body{font-family:"Roboto Condensed",Arial,sans-serif;color:var(--ink)}
  .spread{position:absolute;left:60px;top:38px;width:1080px;height:764px;display:flex;box-shadow:0 6px 24px rgba(0,0,0,.25)}
  .page{position:relative;width:540px;height:764px;background:var(--paper);overflow:hidden}

  /* inner page */
  .goals-header{position:absolute;left:0;top:0;width:540px;height:62px;background:var(--dark)}
  .goals-header h2{position:absolute;left:34px;top:22px;color:var(--yellow);font-size:22px;font-weight:700;font-style:italic}
  .goals-body{position:absolute;left:34px;top:80px;width:470px;font-size:12.4px;line-height:1.34;text-align:justify}
  .goals-body p{margin-bottom:8px}
  .goals-body strong{font-weight:800}
  .tag{display:inline-block;position:relative;background:var(--yellow);font-weight:800;font-size:14px;padding:3px 18px 3px 10px;margin:4px 0 4px -10px;clip-path:polygon(0 0,88% 0,100% 50%,88% 100%,0 100%)}
  .letter{position:absolute;left:0;top:470px;width:540px;height:294px;background:var(--dark);color:#fff;padding:26px 34px;font-size:12.4px;line-height:1.36}
  .letter p{margin-bottom:10px}
  .letter .hl{color:var(--yellow);font-weight:800}

  /* cover */
  .candidate-name{position:absolute;left:30px;top:24px;font-family:"Archivo Black",Arial,sans-serif;font-size:33px;letter-spacing:.3px}
  .portrait{position:absolute;left:20px;top:76px;width:520px;height:556px;background:linear-gradient(160deg,var(--photo-top),var(--photo-bottom))}
  .subtitle{position:absolute;right:0;top:92px;background:var(--yellow);font-weight:800;font-size:24px;padding:6px 18px 6px 20px}
  .list-box{position:absolute;right:0;width:220px;background:var(--yellow);padding:8px 12px;line-height:1.05}
  .list-box b{display:block;font-size:26px;font-weight:800}
  .list-box span{font-size:18px}
  .list-9{top:240px}
  .list-10{top:322px}
  .vote-band{position:absolute;left:20px;top:540px;width:520px;height:92px;background:rgba(28,28,28,.92)}
  .ballots{position:absolute;left:20px;top:14px}
  .vote-call{position:absolute;right:16px;top:10px;color:#fff;font-weight:800;font-size:32px;line-height:1;text-align:right;transform:rotate(-3deg)}
  .org-name{position:absolute;left:0;width:540px;top:660px;text-align:center;font-size:30px;font-weight:400;letter-spacing:.4px}
</style>
</head>
<body>
<div class="spread">
  <section class="page page-inner">
    <header class="goals-header"><h2>Was ich gerne noch bewirken möchte:</h2></header>
    <div class="goals-body">
      <p><strong>Unterstützung der Freiwilligen Feuerwehren</strong> – Unsere Gemeindefeuerwehr wurde in den letzten Jahren mit modernster Technik ausgestattet, die sogar die Verhältnisse anderer Kommunen zum Teil übersteigt. Dennoch werden die Aufgaben im Einsatzdienst für die Kameradinnen und Kameraden immer anspruchsvoller und vielschichtiger. Daher möchte ich mich auch weiterhin dafür stark machen, dass unsere Feuerwehr stets gut ausgestattet ist, denn die Sicherstellung des Brand- und Katastrophenschutzes zählt zu den wichtigsten Aufgaben der Gemeinde.</p>
      <p><strong>Keine Grundsteuererhöhung</strong> – Auch, wenn die dem Gesetzgeber vom Bundesverfassungsgericht aufgetragene Reform der Grundsteuer möglichst aufkommensneutral erfolgen soll, rechnet der Bund der Steuerzahler dennoch mit einer Erhöhung der Grundsteuerhebesätze durch die Kommunen. In Zeiten steigender Kosten kann eine weitere Belastung der Grundstückseigentümer in meinen Augen nicht angehen. Ich möchte mich im Gemeinderat dafür einsetzen, dass von einer Erhöhung des Hebesatzes Abstand genommen wird.</p>
      <span class="tag">Weitere Ziele</span>
      <p>Mehr Verkehrssicherheit • Unterstützung der Gemeinde bei der Errichtung eines Jugend- und Freizeittreffs in Zscherben • Lösung der derzeit zwischen Gemeinde und dem WAZV bestehenden Probleme • Errichtung weiterer Blühwiesen • Verschönerung des Ortsbildes durch Neupflanzungen • eine funktionierende Kommunikation zwischen Einwohnerschaft und Gemeindeverwaltung.</p>
    </div>
    <div class="letter">
      <p>Liebe Einwohnerinnen und Einwohner,</p>
      <p>in den letzten 5 Jahren habe ich mich mit viel Herzblut für unsere Ortschaft und die Gemeinde eingesetzt, Themen und Probleme offen und transparent kommuniziert und mich Ihrer Anliegen stets angenommen. <span class="hl">Gern möchte ich diesen Kurs fortführen und bitte Sie daher zu den Kommunalwahlen am 09.06.2024 um Ihre drei Stimmen!</span></p>
      <p>Sie haben weitere Anregungen oder Fragen? Kontaktieren Sie mich gern!<br><span class="hl">E-Mail: brandt-lukas@postfeld.de | Tel.: 0170/4418265</span></p>
      <p>Herzlichst,<br>Lukas Brandt</p>
    </div>
  </section>

  <section class="page page-cover">
    <h1 class="candidate-name">Lukas Brandt</h1>
    <div class="portrait" role="img" aria-label="Porträtfoto des Kandidaten vor grauem Hintergrund"></div>
    <div class="subtitle">Ihr Kandidat für Zscherben</div>
    <div class="list-box list-9"><b>Listenplatz 9</b><span>Kreistag Saalekreis</span></div>
    <div class="list-box list-10"><b>Listenplatz 10</b><span>Gemeinderat<br>Teutschenthal</span></div>
    <div class="vote-band">
      <svg class="ballots" width="190" height="64" viewBox="0 0 190 64" aria-hidden="true">
        <g fill="none" stroke-linecap="round">
          <g transform="translate(32 32)"><circle r="26" stroke="#fff" stroke-width="5"/><path d="M-16 -16 L16 16 M16 -16 L-16 16" stroke="var(--yellow)" stroke-width="8"/></g>
          <g transform="translate(95 32)"><circle r="26" stroke="#fff" stroke-width="5"/><path d="M-16 -16 L16 16 M16 -16 L-16 16" stroke="var(--yellow)" stroke-width="8"/></g>
          <g transform="translate(158 32)"><circle r="26" stroke="#fff" stroke-width="5"/><path d="M-16 -16 L16 16 M16 -16 L-16 16" stroke="var(--yellow)" stroke-width="8"/></g>
        </g>
      </svg>
      <div class="vote-call">Am 9. Juni<br>UBL wählen!</div>
    </div>
    <div class="org-name">Unabhängige Bürgerliste</div>
  </section>
</div>
</body>
</html>
```